Harvest Bridge Christian Ministry needs a Conference Ad

We are a Christian nonprofit focused on eliminating systemic poverty and helping believers function as ministers in their workplaces. The 2025 Lantern Path Global Conference coming up in October, and we need an ad for social media (facebook, instagram, and X) and our website in order to get people excited to attend! We are looking for a modern and sleek design that incorporates our logo (attached file). You can either put just the butterfly and then write our company name separately somewhere in the design or use it as is (we used Gotham font for the logo). We want to emphasize the joy of in-person connection at the conference, so you could possibly include stock photos of young people gathering together. You could also include the attached photo of our founders in the design and say “with Mel and Dora Quintavan". Also, include the conference dates, which are October 9-12, 2025, and say “come in person or join online”. Lastly, please include the tagline “from the Pellmore Awakening to Worldwide Transformation”. NOTE: I’m attaching AN EXAMPLE I’ve created of how the design could look, which you can feel free to use for inspiration.
Young people on Instagram and facebook
- Gotham

```html
<!DOCTYPE html>
<html lang="en">
<head>
<meta charset="UTF-8">
<title>Harvest Bridge – Lantern Path Global Conference Ads</title>
<link rel="stylesheet" href="https://fonts.googleapis.com/css2?family=Montserrat:wght@300;400;700&display=swap">
<style>
  :root{
    --purple:#3e3558;
    --night:#2a2439;
    --gold:#a88a12;
    --gold-light:#c9a422;
    --white:#ffffff;
    --page:#ffffff;
    --crowd-top:#6b4a33;
    --crowd-warm:#9a6f52;
    --crowd-mid:#4a3a40;
    --crowd-deep:#262633;
    --portrait-glow:#b08468;
    --portrait-mid:#5e3d2c;
    --portrait-edge:#1f1410;
  }
  *{margin:0;padding:0;box-sizing:border-box}
  html,body{width:1200px;height:667px;overflow:hidden;background:var(--page)}
  body{position:relative;font-family:"Montserrat",Arial,sans-serif;text-transform:uppercase}
  .ad{position:absolute;overflow:hidden}
  .block{position:absolute}
  .crowd-photo{background:linear-gradient(160deg,var(--crowd-top) 0%,var(--crowd-warm) 30%,var(--crowd-mid) 62%,var(--crowd-deep) 100%)}
  .founders-photo{background:radial-gradient(ellipse 70% 80% at 58% 55%,var(--portrait-glow) 0%,var(--portrait-mid) 45%,var(--portrait-edge) 100%)}
  .band-purple{background:var(--purple)}
  .band-night{background:var(--night)}
  .center{display:flex;flex-direction:column;align-items:center;justify-content:center;text-align:center}
  .brand{position:absolute;color:var(--white);font-weight:700;line-height:1.05;display:flex;align-items:center;gap:5px;letter-spacing:.02em}
  .brand .mark{display:inline-block;background:var(--white)}
  .headline{color:var(--gold);font-weight:700;letter-spacing:.01em;line-height:1.15}
  .hosts{color:var(--white);font-weight:400;letter-spacing:.08em}
  .dates{color:var(--gold);font-weight:300;line-height:1.05}
  .tagline{color:var(--gold-light);font-weight:400;line-height:1.25}
  .attend{color:var(--white);font-weight:400;line-height:1.25}
  .site{color:var(--white);font-weight:400;letter-spacing:.1em}
  .platform{position:absolute;color:var(--gold);font-weight:300;font-size:17px;letter-spacing:.05em;transform:translateX(-50%)}

  .ig{left:37px;top:36px;width:326px;height:326px}
  .fb{left:420px;top:36px;width:326px;height:580px}
  .xpost{left:799px;top:36px;width:363px;height:204px}
</style>
</head>
<body>

<section class="ad ig">
  <div class="block crowd-photo" style="left:0;top:0;width:326px;height:122px" role="img" aria-label="Photo of smiling young people seated together in a conference audience"></div>
  <div class="brand" style="left:11px;top:12px;font-size:8px"><span class="mark" style="width:8px;height:8px"></span><span>Harvest<br>Bridge</span></div>
  <div class="block band-purple center" style="left:0;top:122px;width:326px;height:82px">
    <div class="headline" style="font-size:16.5px">Be Inspire, Transform, Thrive</div>
    <div class="hosts" style="font-size:13px;margin-top:3px">With Mel &amp; Dora Quintavan</div>
    <div class="dates" style="font-size:25px;margin-top:1px">October 9-12, 2025</div>
  </div>
  <div class="block band-night center" style="left:0;top:204px;width:164px;height:122px;padding:0 4px">
    <div class="tagline" style="font-size:10.5px">From the Pellmore<br>Awakening to<br>Worldwide Transformation</div>
    <div class="attend" style="font-size:10.5px;margin-top:10px">Come in person or<br>join online</div>
    <div class="site" style="font-size:7.5px;margin-top:7px">harvestbridge.org</div>
  </div>
  <div class="block founders-photo" style="left:164px;top:204px;width:162px;height:122px" role="img" aria-label="Portrait of founders Mel and Dora Quintavan"></div>
</section>
<div class="platform" style="left:198px;top:374px">Instagram</div>

<section class="ad fb">
  <div class="block crowd-photo" style="left:0;top:0;width:326px;height:326px" role="img" aria-label="Photo of smiling young people seated together in a conference audience"></div>
  <div class="brand" style="left:16px;top:20px;font-size:12px"><span class="mark" style="width:12px;height:12px"></span><span>Harvest<br>Bridge</span></div>
  <div class="block band-purple center" style="left:0;top:326px;width:326px;height:132px">
    <div class="headline" style="font-size:25px">Be Inspire,<br>Transform, Thrive</div>
    <div class="hosts" style="font-size:13.5px;margin-top:4px">With Mel &amp; Dora Quintavan</div>
    <div class="dates" style="font-size:26px;margin-top:1px">October 9-12, 2025</div>
  </div>
  <div class="block band-night center" style="left:0;top:458px;width:164px;height:122px;padding:0 4px">
    <div class="tagline" style="font-size:10.5px">From the Pellmore<br>Awakening to<br>Worldwide Transformation</div>
    <div class="attend" style="font-size:10.5px;margin-top:10px">Come in person or<br>join online</div>
    <div class="site" style="font-size:7.5px;margin-top:7px">harvestbridge.org</div>
  </div>
  <div class="block founders-photo" style="left:164px;top:458px;width:162px;height:122px" role="img" aria-label="Portrait of founders Mel and Dora Quintavan"></div>
</section>
<div class="platform" style="left:585px;top:630px">Facebook</div>

<section class="ad xpost">
  <div class="block crowd-photo" style="left:0;top:0;width:181px;height:153px" role="img" aria-label="Photo of smiling young people seated together in a conference audience"></div>
  <div class="brand" style="left:12px;top:14px;font-size:7px"><span class="mark" style="width:7px;height:7px"></span><span>Harvest<br>Bridge</span></div>
  <div class="block founders-photo" style="left:0;top:153px;width:68px;height:51px" role="img" aria-label="Portrait of founders Mel and Dora Quintavan"></div>
  <div class="block band-night center" style="left:68px;top:153px;width:113px;height:51px">
    <div class="hosts" style="font-size:9px;line-height:1.2">With Mel &amp; Dora<br>Quintavan</div>
  </div>
  <div class="block band-purple center" style="left:181px;top:0;width:182px;height:204px;padding:0 6px">
    <div class="headline" style="font-size:11.5px;margin-top:18px">Be Inspire,<br>Transform, Thrive</div>
    <div class="dates" style="font-size:18px;color:var(--white);margin-top:10px">October<br>9-12, 2025</div>
    <div class="tagline" style="font-size:7.8px;margin-top:9px">From the Pellmore Awakening<br>to Worldwide<br>Transformation</div>
    <div class="attend" style="font-size:6.6px;margin-top:8px">Come in person or join online</div>
    <div class="site" style="font-size:5.8px;margin-top:6px">harvestbridge.org</div>
  </div>
</section>
<div class="platform" style="left:982px;top:246px">X</div>

</body>
</html>
```